" Mais de 10 anos de experiência, a Quorvix Soluçoes em Tecnologia é especialista no mercado de tecnologia da informaçao, fornecendo serviços e produtos para o mercado empresarial, corporativo e governo. Somos representantes autorizados das melhores marcas, oferecemos soluçoes e alternativas de negócios seguros. Nossos diferenciais sao: foco no cliente, encantamento na hora de atender, rapidez, simplicidade. Alguns de nossos serviços e produtos:  Elaboraçao de projeto para construçao de Data Center;  Implantaçao de Ambientes e projetos para recuperaçao de desastre;  Soluçoes de Backup;  Telefonia IP e Video Conferencia  Soluçoes de alta disponibilidade  Soluçoes de Backup  Vendas de Desktops  Vendas de Tablets  Vendas de Notebooks  vendas de Servidores  vendas de Storages  vendas de Workstations  vendas de Monitores  Outsourcing  Locaçao e vendas de Impressoras  Softwares  Gerenciamento de ativos  Segurança da Informaçao  Gestao de Projetos  Análise e reduçao de Custos com Telecom e TI  Melhorias de Processo. "

```html
<!DOCTYPE html>
<html lang="pt-BR">
<head>
<meta charset="utf-8">
<title>Quorvix Soluções em Tecnologia — Cartão de visita</title>
<link href="https://fonts.googleapis.com/css2?family=Montserrat:wght@400;500;600&display=swap" rel="stylesheet">
<style>
  :root {
    --page: #e9eaec;
    --card-white: #ffffff;
    --navy-dark: #0f2547;
    --navy: #1b3a68;
    --brand-blue: #1f4f86;
    --accent-cyan: #2a9fd6;
    --strip-grey: #c9ccd1;
    --strip-light: #e4e6e9;
    --text-grey: #8a8f96;
    --text-light: #dfe6f0;
  }
  * { box-sizing: border-box; margin: 0; padding: 0; }
  html, body { width: 1200px; height: 1200px; overflow: hidden; }
  body {
    background: var(--page);
    font-family: "Montserrat", sans-serif;
    display: flex; flex-direction: column; align-items: center; justify-content: center;
    gap: 60px;
  }
  .card {
    width: 900px; height: 500px; position: relative; overflow: hidden;
    box-shadow: 0 8px 30px rgba(0,0,0,.15);
  }

  /* Front */
  .card-front { background: var(--card-white); }
  .brand {
    position: absolute; top: 50%; left: 50%; transform: translate(-50%, -60%);
    display: flex; align-items: center; gap: 22px; white-space: nowrap;
  }
  .brand-dot { width: 64px; height: 64px; border-radius: 50%; background: var(--accent-cyan); flex: none; }
  .brand-name {
    font-size: 70px; font-weight: 500; letter-spacing: 4px; color: var(--brand-blue);
  }
  .front-tab {
    position: absolute; left: 0; bottom: 0; width: 300px; height: 48px;
    background: var(--strip-light); display: flex; align-items: center; justify-content: center;
  }
  .front-tab::after {
    content: ""; position: absolute; left: 0; right: 0; bottom: 0; height: 8px; background: var(--strip-grey);
  }
  .web { font-size: 14px; letter-spacing: 2.5px; color: var(--text-grey); white-space: nowrap; }

  /* Back */
  .card-back {
    background: radial-gradient(circle at 30% 40%, var(--navy) 0%, var(--navy-dark) 80%);
    color: var(--text-light);
  }
  .person { position: absolute; top: 44px; left: 56px; }
  .person-name { font-size: 22px; font-weight: 600; letter-spacing: 1px; }
  .person-role { font-size: 14px; margin-top: 6px; opacity: .75; letter-spacing: 1px; }
  .contacts {
    position: absolute; right: 150px; top: 190px; text-align: right;
    font-size: 15px; line-height: 1.9; letter-spacing: .5px; white-space: nowrap;
  }
  .contacts .address { margin-top: 18px; line-height: 1.7; }
  .icon-strip {
    position: absolute; top: 0; right: 0; width: 100px; height: 100%;
    background: linear-gradient(90deg, var(--strip-grey), var(--strip-light));
    display: flex; flex-direction: column; align-items: center; justify-content: center; gap: 26px;
  }
  .icon {
    width: 40px; height: 40px; border-radius: 50%; border: 2px solid #fff;
    display: flex; align-items: center; justify-content: center;
  }
  .icon svg { width: 20px; height: 20px; fill: none; stroke: #fff; stroke-width: 2; stroke-linecap: round; stroke-linejoin: round; }
</style>
</head>
<body>

  <section class="card card-front">
    <div class="brand">
      <span class="brand-dot"></span>
      <span class="brand-name">QUORVIX</span>
    </div>
    <div class="front-tab"><span class="web">www.quorvix-exemplo.com</span></div>
  </section>

  <section class="card card-back">
    <div class="person">
      <p class="person-name">Nome Sobrenome</p>
      <p class="person-role">Diretor Comercial</p>
    </div>
    <div class="contacts">
      <p>tel: (00) 4321-0987</p>
      <p>e-mail: contato@quorvix-exemplo.com</p>
      <p class="address">End: 48 Rua das Palmeiras | Centro | Vila Serena<br>UF | CEP: 00.000-100 | Porto Claro</p>
    </div>
    <div class="icon-strip">
      <span class="icon" aria-label="telefone">
        <svg viewBox="0 0 24 24"><path d="M5 3h4l2 5-2.5 1.5a11 11 0 0 0 6 6L16 13l5 2v4a2 2 0 0 1-2 2A16 16 0 0 1 3 5a2 2 0 0 1 2-2z"/></svg>
      </span>
      <span class="icon" aria-label="e-mail">
        <svg viewBox="0 0 24 24"><rect x="3" y="5" width="18" height="14" rx="2"/><path d="M3 7l9 6 9-6"/></svg>
      </span>
      <span class="icon" aria-label="endereço">
        <svg viewBox="0 0 24 24"><path d="M12 22s7-7 7-12a7 7 0 0 0-14 0c0 5 7 12 7 12z"/><circle cx="12" cy="10" r="2.5"/></svg>
      </span>
    </div>
  </section>

</body>
</html>
```